Corporate Web Redesign Project - coded

We would like redesign/refresh of our current site that would allow us to increase the depth of content and create a high quality impression for visitors.

Current site - http://corvanisystems.com/

A previous web redesign project has improved our site but it has not really reached the level we require.

Our customers are global, blue chip, organisations and a professional, corporate style of site is required.

Please note we would prefer a coded website to a just a design. We are happy to provide a zip of our current site if required.
Updates

                                   

Target Market(s)

Global oil and gas producers, KR, Tamberline, Orvadex etc.

Industry/Entity Type

It Professional

Requirements
Must have
• Design should support the level of content we currently have in the existing sitemap - although it should be expandable a site design for a large / complex site would not be appropriate

All current content / pages to be reflected in design

Must be visually appealing

Intuitive and clear navigation that is expandable

Display a high level of professionalism

Use a consistent palette of colours that complements our logo

Clean and organized layout

A way to capture visitor’s information or Call to action (i.e. contact link or form) on every page

Prominent Contact Information
Should not have
• Flash

```html
<!DOCTYPE html>
<html lang="en">
<head>
<meta charset="utf-8">
<title>Corvani Systems</title>
<link href="https://fonts.googleapis.com/css2?family=Mulish:wght@300;400;600;700&display=swap" rel="stylesheet">
<style>
:root{
  --dark:#303030;
  --darker:#2a2a2a;
  --teal:#3fc9bd;
  --teal-text:#42b8b0;
  --nav-top:#5aa6ab;
  --nav-bottom:#3f8a90;
  --grey-bg:#efefef;
  --text:#8a8a8a;
  --heading:#333;
  --link:#2a9fd6;
  --white:#fff;
}
*{box-sizing:border-box;margin:0;padding:0}
html,body{width:886px;height:1200px;overflow:hidden}
body{position:relative;font-family:"Mulish",sans-serif;background:var(--white);color:var(--text)}
.abs{position:absolute}

.topbar{left:0;top:0;width:886px;height:26px;background:var(--dark)}
.topbar nav{left:95px;top:7px;display:flex;gap:19px;font-size:10px;font-weight:700;color:var(--white)}
.social{top:0;height:26px;width:29px;background:#3c3c3c;border-left:1px solid #262626}

.brand{left:100px;top:60px;display:flex;align-items:center;gap:10px;font-size:22px;font-weight:700;color:#2f7d86}
.brand i{display:block;width:26px;height:26px;border-radius:50%;background:#2f7d86}
.support{left:632px;top:64px;display:flex;gap:10px;align-items:center}
.support .l1{font-size:12px;color:#333}
.support .l1 b{font-weight:600}
.support .l1 em{font-style:italic}
.support .l2{font-size:15px;color:#444;margin-top:2px}

.mainnav{left:82px;top:125px;width:722px;height:37px;background:linear-gradient(var(--nav-top),var(--nav-bottom));border-top:2px solid #7cc0c4;display:flex;align-items:center}
.mainnav a{height:100%;display:flex;align-items:center;justify-content:center;color:var(--white);font-size:12px;font-weight:700;border-right:1px solid #347a80;text-decoration:none}
.mainnav .search-label{color:var(--white);font-size:12px;font-weight:700;width:76px;text-align:center}
.search-box{width:168px;height:21px;background:var(--white);display:flex;align-items:center;justify-content:space-between;padding:0 4px 0 9px;font-size:8px;color:#999}

.hero{left:0;top:163px;width:886px;height:403px;background:linear-gradient(180deg,#7fb2dd 0%,#a9c9e2 45%,#c9b392 62%,#a27a4c 78%,#7a5b3c 100%)}
.hero-panel{left:82px;top:268px;width:367px;height:156px;background:rgba(70,70,70,.85)}
.hero-panel h1{position:absolute;left:16px;top:14px;font-size:29px;line-height:36px;font-weight:400;color:var(--teal);letter-spacing:-1.1px;white-space:nowrap}
.hero-panel p{position:absolute;left:16px;top:56px;width:318px;font-size:10.8px;line-height:15px;color:var(--white)}
.hero-panel .btn{position:absolute;left:20px;top:114px;width:130px;height:29px;background:#eef6fb;color:#333;font-size:13px;display:flex;align-items:center;justify-content:center}
.arrow{width:32px;height:32px;border-radius:50%;background:rgba(120,130,140,.7);display:flex;align-items:center;justify-content:center}

.features{left:82px;top:512px;width:722px;height:176px;background:var(--white)}
.feature{top:13px;width:166px}
.feature .tile{height:79px;background:#e6e6e6;padding:7px;}
.feature .tile div{height:100%;background:#ededed;display:flex;align-items:center;justify-content:center}
.feature.active .tile div{background:var(--teal)}
.feature h3{margin-top:14px;font-size:10.5px;font-weight:600;color:var(--teal-text);text-align:center;white-space:nowrap}
.feature p{margin-top:4px;font-size:8.6px;line-height:12px;text-align:center;color:#888}

.about{left:0;top:688px;width:886px;height:262px;background:var(--grey-bg);border-top:1px solid #e2e2e2}
.about h2{position:absolute;left:94px;top:27px;font-size:25px;font-weight:300;color:#333}
.about .body{position:absolute;left:94px;top:69px;width:442px;font-size:9.3px;line-height:16.2px;color:#999}
.about .body p+p{margin-top:16px}
.about .divider{position:absolute;left:544px;top:42px;width:1px;height:206px;background:#ddd}
.news{position:absolute;left:571px;top:36px;width:225px}
.news h2{position:static;font-size:17px;font-weight:400;color:#222}
.news article{margin-top:14px}
.news h4{font-size:9.6px;font-weight:400;color:var(--teal-text);white-space:nowrap}
.news time{display:block;margin-top:4px;font-size:8px;color:#333}
.news p{margin-top:4px;font-size:8.3px;line-height:14.5px;color:#999}
.news p a{color:var(--link);text-decoration:none}

.footer{left:0;top:950px;width:886px;height:208px;background:var(--dark);border-top:4px solid var(--teal)}
.footer .notch{position:absolute;left:430px;top:-1px}
.fcol{top:44px;width:142px}
.fcol h5{height:20px;font-size:10.5px;font-weight:700;color:var(--white)}
.fcol .rule{height:1px;background:#4a4a4a;margin-bottom:18px}
.fcol ul{list-style:none;font-size:9.8px;line-height:18.5px;color:#c8c8c8;white-space:nowrap}
.field{width:155px;height:20px;background:#f4f4f4;border-radius:2px;font-size:8.6px;color:#555;padding:5px 9px;margin-bottom:8px}
.field.msg{height:36px}
.submit{width:53px;height:18px;background:var(--teal);border-radius:2px;color:var(--white);font-size:9.5px;font-weight:700;display:flex;align-items:center;justify-content:center}

.bottombar{left:0;top:1158px;width:886px;height:42px;background:var(--darker);border-top:1px solid #3a3a3a;font-size:10px;color:var(--white)}
</style>
</head>
<body>

<header>
  <div class="abs topbar">
    <nav class="abs"><span>Home</span><span>About Us</span><span>Services</span><span>Products</span></nav>
    <span class="abs social" style="left:700px"></span>
    <span class="abs social" style="left:731px"></span>
    <span class="abs social" style="left:762px"></span>
  </div>

  <div class="abs brand"><i></i><span>Corvani Systems</span></div>

  <div class="abs support">
    <svg width="32" height="32" viewBox="0 0 32 32" aria-hidden="true">
      <path d="M5 18v-3a11 11 0 0 1 22 0v3" fill="none" stroke="#3f8a90" stroke-width="2.5"/>
      <rect x="3" y="16" width="6" height="10" rx="2" fill="#3f8a90"/>
      <rect x="23" y="16" width="6" height="10" rx="2" fill="#3f8a90"/>
      <path d="M26 26q0 4-8 4" fill="none" stroke="#3f8a90" stroke-width="2"/>
    </svg>
    <div>
      <div class="l1"><b>24/7</b> <em>Online Support</em></div>
      <div class="l2">1-800-555-0142</div>
    </div>
  </div>

  <nav class="abs mainnav">
    <a style="width:83px">Home</a>
    <a style="width:78px">News</a>
    <a style="width:98px">About Us</a>
    <a style="width:98px">Solutions</a>
    <a style="width:107px">Contact Us</a>
    <span class="search-label">Search</span>
    <div class="search-box"><span>Enter Keyword</span>
      <svg width="14" height="14" viewBox="0 0 14 14" aria-hidden="true"><circle cx="6" cy="6" r="4.2" fill="none" stroke="#111" stroke-width="2"/><path d="M9 9l4 4" stroke="#111" stroke-width="2.2"/></svg>
    </div>
  </nav>
</header>

<section class="abs hero" role="img" aria-label="Photo of an oil pump jack and storage tanks on open prairie under a blue sky"></section>
<div class="abs hero-panel">
  <h1>Lorem Ipsum simplement</h1>
  <p>Lorem ipsum dolor sit amet, consectetuer adipiscing elit, sed diam nonummy nibh euismod tincidunt ut laoreet dolore magnaam erat voluat isi enim ad minim veniam .</p>
  <span class="btn">Learn More</span>
</div>
<span class="abs arrow" style="left:33px;top:314px"><svg width="10" height="14" viewBox="0 0 10 14"><path d="M8 1L2 7l6 6" fill="none" stroke="#ddd" stroke-width="1.6"/></svg></span>
<span class="abs arrow" style="left:780px;top:314px"><svg width="10" height="14" viewBox="0 0 10 14"><path d="M2 1l6 6-6 6" fill="none" stroke="#fff" stroke-width="1.6"/></svg></span>

<section class="abs features">
  <div class="abs feature active" style="left:13px">
    <div class="tile"><div><svg width="28" height="26" viewBox="0 0 28 26"><rect x="1" y="14" width="6" height="11" fill="#fff"/><rect x="11" y="8" width="6" height="17" fill="#fff"/><rect x="21" y="1" width="6" height="24" fill="#fff"/></svg></div></div>
    <h3>TIME &amp; COST ESTIMATION</h3>
    <p>Dolore eu feugiat nulla facilisis at vero eros et accumsan</p>
  </div>
  <div class="abs feature" style="left:190px">
    <div class="tile"><div><svg width="20" height="26" viewBox="0 0 20 26"><rect x="1" y="1" width="18" height="24" rx="2" fill="none" stroke="#777" stroke-width="2"/><rect x="4" y="4" width="12" height="5" fill="#777"/><g fill="#777"><rect x="4" y="12" width="3" height="3"/><rect x="8.5" y="12" width="3" height="3"/><rect x="13" y="12" width="3" height="3"/><rect x="4" y="17" width="3" height="3"/><rect x="8.5" y="17" width="3" height="3"/><rect x="13" y="17" width="3" height="3"/></g></svg></div></div>
    <h3>MATERIALS &amp; COST CONTRO</h3>
    <p>Dolore eu feugiat nulla facilisis at vero eros et accumsan</p>
  </div>
  <div class="abs feature" style="left:367px">
    <div class="tile"><div><svg width="36" height="26" viewBox="0 0 36 26"><path d="M1 3h14q3 0 3 3v19q0-3-3-3H1z M35 3H21q-3 0-3 3v19q0-3 3-3h14z" fill="none" stroke="#777" stroke-width="2"/><path d="M5 9h9M5 13h9M5 17h9M22 9h9M22 13h9M22 17h9" stroke="#777" stroke-width="1.5"/></svg></div></div>
    <h3>LESSONS LEARNED</h3>
    <p>Dolore eu feugiat nulla facilisis at vero eros et accumsan</p>
  </div>
  <div class="abs feature" style="left:544px">
    <div class="tile"><div><svg width="24" height="26" viewBox="0 0 24 26"><path d="M15 3a5 5 0 0 0-4 7L3 18l3 3 8-8a5 5 0 0 0 7-4l-3 1-2-2 1-3z" fill="#777"/><rect x="2" y="22" width="20" height="3" fill="#777"/></svg></div></div>
    <h3>SERVICES &amp; CONSULTING</h3>
    <p>Dolore eu feugiat nulla facilisis at vero eros et accumsan</p>
  </div>
</section>

<section class="abs about">
  <h2>Welcome to Corvani Systems</h2>
  <div class="body">
    <p>Lorem ipsum dolor sit amet, consectetuer adipiscing elit, sed diam nonummy nibh euismod tinci-dunt ut laoreet dolore magna aliquam erat volutpat. Ut wisi enim ad minim veniam, quis nostrud exerci tation ullamcorper suscipit lobortis nisl ut aliquip ex ea commodo consequat. Duis autem vel eum iriure dolor in hendrerit in vulputate velit esse molestie consequat,</p>
    <p>Dolore eu feugiat nulla facilisis at vero eros et accumsan et iusto odio dignissim qui blandit praesent luptatum zzril delenit augue duis dolore te feugait nulla facilisi. Nam liber tempor cum soluta nobis eleifend option congue nihil imperdiet doming id quod mazim placerat facer possim assum. Typi non habent claritatem insitam; est usus legentis in iis qui facit eorum claritatem. Investiga-tiones demonstraverunt lectores legere me lius quod ii legunt saepius.</p>
  </div>
  <div class="divider"></div>
  <div class="news">
    <h2>Latest News</h2>
    <article>
      <h4>Lorem ipsum dolor sit ametsfs, consectetuer</h4>
      <time>Novermber 01, 2012</time>
      <p>Lorem ipsum dolor sit amet, consectetuer adipiscing elit, sed diam nonummy nibh euismod tincidunt. ut laoreet dolore. <a>Read More</a></p>
    </article>
    <article>
      <h4>Lorem ipsum dolor sit ametsfs, consectetuer</h4>
      <time>Novermber 01, 2012</time>
      <p>Lorem ipsum dolor sit amet, consectetuer adipiscing elit, sed diam nonummy nibh euismod tincidunt. ut laoreet dolore. <a>Read More</a></p>
    </article>
  </div>
</section>

<footer class="abs footer">
  <svg class="notch" width="26" height="15" viewBox="0 0 26 15" aria-hidden="true"><path d="M0 0h26L13 15z" fill="#3fc9bd"/></svg>
  <div class="abs fcol" style="left:98px">
    <h5></h5><div class="rule"></div>
    <ul><li>18 Kelmont Row</li><li>Dunmarr</li><li>DM4 2QT</li><li>Phone:+44(0)1632 960417</li><li>Email: eu@corvanisystems.com</li></ul>
  </div>
  <div class="abs fcol" style="left:270px">
    <h5>NORTH AMERICA</h5><div class="rule"></div>
    <ul><li>4100 Ridgefield Pkwy</li><li>Suite 210</li><li>Bramford, TX 75501</li><li>Phone:(555) 314 7720</li><li>Email: us@corvanisystems.com</li></ul>
  </div>
  <div class="abs fcol" style="left:441px;width:163px">
    <h5>QUICK CONTACT</h5><div class="rule"></div>
    <div class="field">Full Name</div>
    <div class="field">Email</div>
    <div class="field msg">Message</div>
    <div class="submit">Submit</div>
  </div>
  <div class="abs fcol" style="left:630px;width:163px">
    <h5>SITE MAP</h5><div class="rule"></div>
    <ul><li>Praesent luptatum delen</li><li>it augue duis dolore</li><li>Praesent luptatum delen</li><li>it augue duis dolore</li><li>Praesent luptatum delen</li></ul>
  </div>
</footer>

<div class="abs bottombar">
  <span class="abs" style="left:96px;top:15px">Copyright 2013 Website Name. All Rights Reserved.</span>
  <span class="abs" style="left:634px;top:16px">Privacy Policy | Terms &amp; Condition</span>
</div>

</body>
</html>
```